Combat Sports news website design

Redesigning our existing website to make it more modern, responsive and suitable for our needs. The design needs to take in to account all aspects of our current website structure and services. View the existing website at https://www.bramblewire.co.nz

Particular attention should be paid to our livestream service, which is growing and needs to be much more user friendly to the current experience.

The homepage, article listings and article pages need designs.

Target Market(s)

Combat sports fans

Industry/Entity Type

Media

Coding

Coded - Design and coding required

Number of Pages Required

5+ page

Font styles to use
Sans Serif

Requirements
Must have
• All the functionality of the existing website must be taken in to account, and improved upon.
New design must incorporate our existing logo/colour scheme as this has only just been designed.

```html
<!DOCTYPE html>
<html lang="en">
<head>
<meta charset="utf-8">
<title>Bramble Wire – Combat Sports News</title>
<link href="https://fonts.googleapis.com/css2?family=Roboto:wght@400;500;700;900&display=swap" rel="stylesheet">
<style>
:root{
  --dark:#212327;
  --red:#b3191f;
  --text:#222;
  --muted:#555;
  --line:#e4e4e4;
  --white:#fff;
}
*{box-sizing:border-box;margin:0;padding:0}
html,body{width:1200px;height:3450px;overflow:hidden}
body{position:relative;font-family:'Roboto',sans-serif;color:var(--text);background:var(--white)}
.abs{position:absolute}
.ph{display:block}
.topbar{left:0;top:0;width:1200px;height:90px;background:var(--dark)}
.brand{left:100px;top:10px;color:var(--white);font-weight:900;font-size:29px;line-height:32px;letter-spacing:1px}
.toplinks{left:281px;top:36px;display:flex;gap:26px;color:var(--white);font-size:15px}
.search{left:532px;top:27px;width:374px;height:38px;background:#303338;border-radius:3px;color:#ddd;font-size:12.5px;padding:11px 16px}
.search svg{position:absolute;right:14px;top:10px}
.signin{left:927px;top:36px;color:var(--white);font-size:15px;font-weight:500}
.register{left:987px;top:30px;width:112px;height:32px;background:var(--red);border-radius:16px;color:var(--white);font-size:15px;font-weight:500;text-align:center;line-height:32px}
.mainnav{left:0;top:90px;width:1200px;height:47px;background:var(--red);display:flex;align-items:center;padding-left:101px;color:var(--white);font-size:15.5px;font-weight:500}
.mainnav span.sep{margin:0 25px;opacity:.9}
.slide{overflow:hidden}
.slide .cap{position:absolute;left:8px;bottom:10px;color:var(--white);font-size:13.5px;font-weight:500;line-height:18px}
.fade{opacity:.45}
.arrow{top:318px}
.post{left:103px;width:720px;height:288px}
.post .ph{position:absolute;left:0;top:0;width:254px;height:288px}
.post h2{position:absolute;left:270px;top:18px;font-size:18.5px;font-weight:500}
.post .date{position:absolute;left:270px;top:56px;font-size:14px;display:flex;align-items:center;gap:7px}
.post p{position:absolute;left:270px;top:88px;width:450px;font-size:12.3px;line-height:25px;color:var(--muted)}
.btn{background:var(--red);color:var(--white);font-weight:500;font-size:14px;text-align:center;border-radius:3px}
.post .btn{position:absolute;left:274px;top:232px;width:126px;height:41px;line-height:41px}
.more{left:285px;top:1942px;width:343px;height:46px;background:#e9eaec;border-radius:3px;font-size:15px;text-align:center;line-height:46px;color:#222}
.card{background:var(--white);box-shadow:0 1px 6px rgba(0,0,0,.12)}
.tips{left:849px;top:589px;width:248px;height:259px;padding:14px 16px}
.tips h3{font-size:22px;font-weight:500;margin-bottom:10px}
.tips p{font-size:12px;line-height:22.5px;color:#333}
.tips a{color:#1e7fd6;text-decoration:underline}
.sidehead{background:var(--red);color:var(--white);font-size:20px;font-weight:700;padding:0 8px;height:47px;line-height:50px}
.popular{left:852px;top:886px;width:246px;height:373px}
.pop{display:flex;gap:7px;margin:10px 10px 0 10px;padding-bottom:9px;border-bottom:1px solid var(--line)}
.pop .ph{width:68px;height:68px;flex:none}
.pop b{display:block;font-size:12px;font-weight:500;line-height:16px}
.pop small{display:block;font-size:10.5px;line-height:15px;color:#555;margin-top:2px}
.popular .btn{margin:14px 0 0 10px;width:96px;height:30px;line-height:30px;font-size:11.5px}
.poll{left:852px;top:1283px;width:246px;height:300px}
.poll .q{font-size:13.5px;padding:13px 12px;border-bottom:1px solid var(--line)}
.opt{margin:0 4px 0 14px;padding:9px 0;font-size:15px;border-bottom:1px solid var(--line);display:flex;align-items:center;gap:8px}
.opt i{width:13px;height:13px;border:2px solid #222;border-radius:50%}
.pollbtns{display:flex;gap:4px;margin:14px 0 0 15px}
.pollbtns .btn{height:30px;line-height:30px;font-size:11.5px;padding:0 13px}
.ad{border:1px solid #e3e3e3;background:var(--white);font-size:12px;color:#333}
.sechead{left:100px;font-size:24.5px;font-weight:700}
.live{top:2130px;width:241px;height:318px;overflow:hidden}
.live .tag{position:absolute;left:62px;top:210px;width:118px;height:30px;background:var(--red);color:var(--white);font-size:12px;text-align:center;line-height:30px;border-radius:2px}
.live .title{position:absolute;left:18px;right:18px;top:250px;color:var(--white);font-size:18px;font-weight:500;text-align:center;line-height:23px}
.rel{width:241px}
.rel .ph{width:241px;height:169px}
.rel p{font-size:14.5px;line-height:25px;padding:10px 3px 0;color:#222}
.footer{left:0;top:3150px;width:1200px;height:300px;background:var(--dark);color:var(--white)}
.fbrand{left:100px;top:62px;font-weight:900;font-size:44px;line-height:46px}
.fcol{top:60px;font-size:13.5px;line-height:23px}
.fcol h4{color:#e0393e;font-size:16px;font-weight:500;margin-bottom:4px}
.fmail{left:100px;top:210px;font-size:15px;display:flex;align-items:center;gap:8px}
.frule{left:100px;top:248px;width:1000px;height:1px;background:#444}
.copy{left:0;top:266px;width:1200px;text-align:center;font-size:15px}
</style>
</head>
<body>

<header>
  <div class="abs topbar"></div>
  <div class="abs brand">BRAMBLE<br>WIRE</div>
  <nav class="abs toplinks"><span>About</span><span>Advertise</span><span>Contact</span></nav>
  <div class="abs search">Enter keyword to search...
    <svg width="18" height="18" viewBox="0 0 18 18"><circle cx="7.5" cy="7.5" r="6" fill="none" stroke="#ccc" stroke-width="1.6"/><line x1="12" y1="12" x2="17" y2="17" stroke="#ccc" stroke-width="1.6"/></svg>
  </div>
  <div class="abs signin">Sign In</div>
  <div class="abs register">Register</div>
  <nav class="abs mainnav">
    <span>HOME</span><span class="sep">|</span><span>MMA</span><span class="sep">|</span><span>KICKBOXING</span><span class="sep">|</span><span>BOXING</span><span class="sep">|</span><span>WRESTLING</span><span class="sep">|</span><span>OCTA</span><span class="sep">|</span><span>PACIFICFC</span><span class="sep">|</span><span>LIVE EVENTS</span><span class="sep">|</span><span>CONTACT US</span>
  </nav>
</header>

<section class="slider">
  <div class="abs slide fade" style="left:0;top:137px;width:228px;height:387px;background:linear-gradient(160deg,#7d7a78,#4a4645)" role="img" aria-label="Fighter holding a championship belt"></div>
  <div class="abs slide" style="left:230px;top:137px;width:226px;height:200px;background:linear-gradient(160deg,#5a5a5a,#1b1b1b)" role="img" aria-label="Black and white photo of a fighter">
    <div class="cap">Hayes Tolland with quick<br>turnaround into Summit</div></div>
  <div class="abs slide" style="left:230px;top:342px;width:226px;height:182px;background:linear-gradient(160deg,#6e6a5e,#2d2a26)" role="img" aria-label="Fighter raising her arm in victory">
    <div class="cap">Rise to Fight 9 Results: Mack<br>Jenner wins RTF9 debut</div></div>
  <div class="abs slide" style="left:458px;top:137px;width:339px;height:387px;background:linear-gradient(160deg,#4b3b86,#2d5f9f 55%,#1f2b3f)" role="img" aria-label="Two kickboxers exchanging strikes in the ring">
    <div class="cap" style="left:17px;bottom:14px">
      <div style="font-size:11.5px;margin-bottom:6px">Monday 26 Apr, 2021</div>
      <div style="font-size:19.5px;margin-bottom:6px">Ironbark Fight Night results</div>
      <div style="font-size:10px;line-height:16px;font-weight:400">Last night, Saturday, April 24, South Island Lee Gray's<br>Dominic 'Ranger' Reeve put on a masterful</div></div></div>
  <div class="abs slide" style="left:799px;top:137px;width:171px;height:387px;background:linear-gradient(160deg,#8a7560,#3b3431)" role="img" aria-label="Fighter posing with a title belt">
    <div class="cap">Hayes Tolland with quick<br>turnaround into Summit</div></div>
  <div class="abs slide fade" style="left:972px;top:137px;width:228px;height:387px;background:linear-gradient(160deg,#6b6b73,#33343b)" role="img" aria-label="Fighter standing ringside"></div>
  <svg class="abs arrow" style="left:196px" width="18" height="28" viewBox="0 0 18 28"><path d="M15 2 L4 14 L15 26" fill="none" stroke="#111" stroke-width="3.5"/></svg>
  <svg class="abs arrow" style="left:980px" width="18" height="28" viewBox="0 0 18 28"><path d="M3 2 L14 14 L3 26" fill="none" stroke="#111" stroke-width="3.5"/></svg>
</section>

<main>
  <article class="abs post" style="top:592px">
    <div class="ph" style="background:linear-gradient(160deg,#6a6a6a,#1d1d1d)" role="img" aria-label="Fighter with arms crossed at a press event"></div>
    <h2>Plans for Kane Ridley to fight at OCTA 263</h2>
    <div class="date"><svg width="14" height="14" viewBox="0 0 14 14"><rect x="1" y="2" width="12" height="11" fill="none" stroke="#c0272d" stroke-width="1.4"/><line x1="1" y1="5.5" x2="13" y2="5.5" stroke="#c0272d" stroke-width="1.4"/></svg>Thursday 22 Apr, 2021</div>
    <p>Kane Ridley vs. Dale Dorsey is in the works for OCTA 263 OCTA 263 is close to finalising the lightweight matchup for the June 12 pay-per-view event, which takes place at a location and venue to be announced. New Zealand's Ridley (9-1 MMA, 3-0 OCTA) is coming into the potential fight riding a six-fight winning streak.</p>
    <div class="btn">READ MORE</div>
  </article>

  <article class="abs post" style="top:933px">
    <div class="ph" style="background:linear-gradient(160deg,#8a6f55,#3a2c26)" role="img" aria-label="Two kickboxers trading kicks in the ring"></div>
    <h2>Callum Carides fights his way to the top</h2>
    <div class="date"><svg width="14" height="14" viewBox="0 0 14 14"><rect x="1" y="2" width="12" height="11" fill="none" stroke="#c0272d" stroke-width="1.4"/><line x1="1" y1="5.5" x2="13" y2="5.5" stroke="#c0272d" stroke-width="1.4"/></svg>Monday, 15 October 2018</div>
    <p>Strike Lab's Callum Carides wants to keep the momentum going after defeated Combat Foundry's Sheldon Marsh by 3rd round TKO at Aftermath of Knees. The fight started competitively, but in the second round the leg kicks of Carides began to take their toll, visibly hobbling Marsh, who battled gamely on.</p>
    <div class="btn">READ MORE</div>
  </article>

  <article class="abs post" style="top:1267px">
    <div class="ph" style="background:linear-gradient(160deg,#9fb2bf,#3c4a55)" role="img" aria-label="Portrait of a fighter outdoors"></div>
    <h2>Adeyemi to defend title at OCTA 263</h2>
    <div class="date"><svg width="14" height="14" viewBox="0 0 14 14"><rect x="1" y="2" width="12" height="11" fill="none" stroke="#c0272d" stroke-width="1.4"/><line x1="1" y1="5.5" x2="13" y2="5.5" stroke="#c0272d" stroke-width="1.4"/></svg>Saturday, 6 October 2018</div>
    <p>OCTA champion Elias Adeyemi is the latest Kiwi announced to fight at OCTA 263. Adeyemi will defend his middleweight title against Italian Mario Vetrano in June. Adeyemi has not stepped into the octagon since suffering the first defeat of his mixed martial arts career in a recent light-heavyweight title bout against Polish champion Jan Brazek, reports Kiwi Wire.</p>
    <div class="btn">READ MORE</div>
  </article>

  <article class="abs post" style="top:1608px">
    <div class="ph" style="background:linear-gradient(160deg,#4a7fc0,#152a52)" role="img" aria-label="Boxing legend holding a championship belt overhead"></div>
    <h2>Boxing legend Mick Tarrant returns to PWX Detonate</h2>
    <div class="date"><svg width="14" height="14" viewBox="0 0 14 14"><rect x="1" y="2" width="12" height="11" fill="none" stroke="#c0272d" stroke-width="1.4"/><line x1="1" y1="5.5" x2="13" y2="5.5" stroke="#c0272d" stroke-width="1.4"/></svg>Thursday, 6 September 2018</div>
    <p>Ahead of this week's episode of PWX DETONATE, Pro Wrestling X announced that boxing legend Mick Tarrant will be returning for an appearance during its live show on Strikeline TV. No stranger to the squared circle, Tarrant appeared at the ALL OR NOTHING PPV event in May 2020, followed by a memorable PWX DETONATE episode where he brawled</p>
    <div class="btn">READ MORE</div>
  </article>

  <div class="abs more">⁙ More Stories</div>
</main>

<aside>
  <div class="abs card tips">
    <h3>Got A News Tips?</h3>
    <p>Lorem ipsum lor sit amet, consectetur adipiscing elit, sedo eiusmod tempor incididunt ut labore et dolore magna aliqua. Ut enim ad minim veniam, quis nostrud exercitation ullamco laboris nisi ut aliquip ex ea modo consequat. Duis aute irure dolor in reprehenderit in voluptate velit esse <a>Send News Tips</a></p>
  </div>

  <div class="abs card popular">
    <div class="sidehead">POPULAR POSTS</div>
    <div class="pop"><div class="ph" style="background:linear-gradient(160deg,#5b6a86,#222)" role="img" aria-label="Fighter in the ring"></div><div><b>Hallworth aiming for international fight career</b><small>Rob Hallworth (18-3, 9KO) has been involved with fight</small></div></div>
    <div class="pop"><div class="ph" style="background:linear-gradient(160deg,#6a5f70,#222)" role="img" aria-label="Boxers at a weigh-in"></div><div><b>Jace Tiller: snake in the tall grass</b><small>Last Saturday, October 31 at Crown of Crowns 9, Jace Tiller</small></div></div>
    <div class="pop" style="border:none"><div class="ph" style="background:linear-gradient(160deg,#7a3a3a,#222)" role="img" aria-label="Charity fight night poster"></div><div><b>Steel Fist 10 Charity Fight Night tonight</b><small>NKR Promotions is bringing its 10th Steel Fist fight night to</small></div></div>
    <div class="btn">VIEW MORE</div>
  </div>

  <div class="abs card poll">
    <div class="sidehead">OPINION POLL</div>
    <div class="q">What combat sport do you prefer?</div>
    <div class="opt"><i></i>MMA</div>
    <div class="opt"><i></i>Wrestling</div>
    <div class="opt"><i></i>Kickboxing</div>
    <div class="opt"><i></i>Muay Thai</div>
    <div class="pollbtns"><div class="btn">VOTE</div><div class="btn">VIEW RESULTS</div></div>
  </div>

  <div class="abs" style="left:866px;top:1620px;width:218px;height:175px">
    <div style="display:flex;gap:8px;align-items:center;font-size:11.5px"><span style="width:26px;height:22px;background:#222;display:inline-block"></span><span>Online Exclusive Sale<br><span style="font-size:8px;color:#888">lensly.com</span></span></div>
    <div class="ad abs" style="left:0;top:36px;width:212px;height:136px;padding:6px">
      <div style="height:80px;background:linear-gradient(90deg,#f4f4f4,#e8e6dc)" role="img" aria-label="Eyeglasses product"></div>
      <div style="margin-top:6px;font-size:13px">Lensly Air Slim Frame</div>
      <div style="display:flex;justify-content:space-between;font-size:9px;color:#777;margin-top:3px">₹2,800<span style="background:#111;color:#fff;padding:2px 28px;font-weight:700">OPEN</span></div>
    </div>
  </div>
  <div class="abs ad" style="left:866px;top:1818px;width:212px;height:176px;padding:12px 14px">
    <div style="display:flex;gap:8px;font-size:13px"><span style="width:34px;height:34px;background:#f0a53a;flex:none"></span>Fun With<br>Papercraft Origami</div>
    <div style="font-size:8.5px;color:#777;line-height:13px;margin-top:10px">Best Indoor Activity For Kids To Improve their Creativity With Papercraft Origami Sheets<br>Papercraft</div>
    <div style="margin-top:12px;background:#555;color:#fff;font-size:10px;text-align:center;height:24px;line-height:24px;border-radius:3px">Open</div>
  </div>
</aside>

<section>
  <h2 class="abs sechead" style="top:2080px">LIVE STREAMING</h2>
  <div class="abs live" style="left:99px;background:linear-gradient(180deg,#2d3136,#0f1114)" role="img" aria-label="Muay Thai fighters event poster"><div class="tag">Event HERE!</div><div class="title">Summit - Muay Thai Warrior Series</div></div>
  <div class="abs live" style="left:352px;background:linear-gradient(180deg,#7a1d1d,#1b1010)" role="img" aria-label="Female fighter in the ring"><div class="tag">Event HERE!</div><div class="title">Fighting for Blood - 5 reasons why female</div></div>
  <div class="abs live" style="left:605px;background:linear-gradient(180deg,#4a76b8,#1a2a44)" role="img" aria-label="Two boxers face to face"><div class="tag">Event HERE!</div><div class="title">Harbourside Showdown just days away</div></div>
  <div class="abs live" style="left:858px;background:linear-gradient(180deg,#8a6e50,#1d1712)" role="img" aria-label="Fighter speaking at a press conference"><div class="tag">Event HERE!</div><div class="title">Adeyemi issues apology over 'rape'</div></div>
</section>

<section>
  <h2 class="abs sechead" style="top:2537px">RELATED POSTS</h2>
  <div class="abs rel" style="left:99px;top:2578px"><div class="ph" style="background:linear-gradient(160deg,#555,#1a1a1a)" role="img" aria-label="Fighter with a title belt"></div><p>Aaron Tane flourishing under tutelage of Dan Hollister</p></div>
  <div class="abs rel" style="left:352px;top:2578px"><div class="ph" style="background:linear-gradient(160deg,#6a6a6a,#222)" role="img" aria-label="Crowd of fighters celebrating"></div><p>World-class action planned for Rise to Fight 9</p></div>
  <div class="abs rel" style="left:605px;top:2578px"><div class="ph" style="background:linear-gradient(160deg,#9a8f8a,#3a2323)" role="img" aria-label="Kickboxers sparring in a gym ring"></div><p>Yasir Yalin not underestimating Rob Hallworth</p></div>
  <div class="abs rel" style="left:858px;top:2578px"><div class="ph" style="background:linear-gradient(160deg,#6b3b9a,#b02a3a)" role="img" aria-label="Fighter with championship belt on stage"></div><p>Aaron Tane defends his pro bantamweight title at VFC 48</p></div>
  <div class="abs rel" style="left:99px;top:2834px"><div class="ph" style="background:linear-gradient(160deg,#7a6a55,#221e1a)" role="img" aria-label="Group of fighters event poster"></div><p>Aussie fighters to feature in HORIZON: INSIDE THE GRID</p></div>
  <div class="abs rel" style="left:352px;top:2834px"><div class="ph" style="background:linear-gradient(160deg,#c0652a,#1f1d3a)" role="img" aria-label="Wrestler on stage with pyrotechnics"></div><p>PWX announces winners to inaugural awards</p></div>
  <div class="abs rel" style="left:605px;top:2834px"><div class="ph" style="background:linear-gradient(160deg,#9a8a7a,#3b2b22)" role="img" aria-label="Fighters training in a gym ring"></div><p>Sam Perkins ready for war at Summit MTW</p></div>
  <div class="abs rel" style="left:858px;top:2834px"><div class="ph" style="background:linear-gradient(160deg,#3f6bb0,#1e2a40)" role="img" aria-label="Boxer with his coaches"></div><p>Summer Games: Boxer David Nyland to fulfil his Games dream</p></div>
</section>

<footer class="abs footer">
  <div class="abs fbrand">BRAMBLE<br>WIRE</div>
  <div class="abs fmail"><svg width="16" height="12" viewBox="0 0 16 12"><rect x="1" y="1" width="14" height="10" fill="none" stroke="#fff" stroke-width="1.4"/><path d="M1 1 L8 7 L15 1" fill="none" stroke="#fff" stroke-width="1.4"/></svg>newsdesk@bramblewire.co.nz</div>
  <div class="abs fcol" style="left:482px"><h4>COMMUNITY</h4>About Us<br>Contact Us<br>Login<br>Sign Up<br>FAQ</div>
  <div class="abs fcol" style="left:738px"><h4>RESOURCES</h4>Download<br>Help Center<br>Events<br>About Us</div>
  <div class="abs fcol" style="left:987px"><h4>RESOURCES</h4>Bramble Wire Home<br>Request an Invite<br>Privacy Policy
    <div style="display:flex;gap:10px;margin-top:10px"><span style="width:12px;height:12px;border-radius:50%;background:#fff"></span><span style="width:12px;height:12px;border-radius:50%;background:#fff"></span><span style="width:12px;height:12px;border-radius:50%;background:#fff"></span></div></div>
  <div class="abs frule"></div>
  <div class="abs copy">© 2021 Bramble Wire. All Rights Reserved.</div>
</footer>

</body>
</html>
```